Billboard design for a new container self storage

I’m after a sign designing for a new container storage opening. located in the heart of Scunthorpe. Open 24/7. Brand new containers. On site security. Best prices guaranteed

Open 24/7
Safe secure self storage
Best prices Guaranteed
Site address
Hollin Row
Scunthorpe
DN17 3QR
Also include next left and an arrow
Dark green/ grey and fluorescent lime green

Contact - info@brindlevaults.co.uk
07924163587

Requirements
Must have
• Instagram logo @Brindleselfstorage

```html
<!DOCTYPE html>
<html lang="en">
<head>
<meta charset="utf-8">
<title>Brindle – Container Storage Opening Billboard</title>
<link href="https://fonts.googleapis.com/css2?family=Montserrat:wght@500;600;800;900&family=Oswald:wght@400&display=swap" rel="stylesheet">
<style>
  :root{
    --lime:#dcff3c;
    --green-bright:#4ea81c;
    --green-mid:#2f7416;
    --green-dark:#1d3a1a;
    --ink:#1e3320;
    --white:#ffffff;
    --card-shade:#dcdcdc;
    --bg-light:#b9b9b9;
    --bg-dark:#6d6d6d;
  }
  *{box-sizing:border-box;margin:0;padding:0}
  html,body{width:1052px;height:1200px;overflow:hidden}
  body{
    background:linear-gradient(90deg,var(--bg-light),var(--bg-dark));
    font-family:"Montserrat",sans-serif;
    position:relative;
  }
  .billboard{
    position:absolute;left:26px;top:351px;width:1000px;height:497px;
    overflow:hidden;
    box-shadow:14px 16px 18px rgba(0,0,0,.45);
  }
  .hero{
    position:absolute;left:0;top:0;width:1000px;height:267px;
    background:
      linear-gradient(180deg,rgba(0,0,0,0) 0%,rgba(0,0,0,0) 35%,rgba(18,40,16,.95) 100%),
      linear-gradient(90deg,var(--green-mid),var(--green-bright) 60%,var(--green-mid));
  }
  .brand{
    position:absolute;left:30px;top:40px;width:180px;
    display:flex;flex-direction:column;align-items:center;gap:10px;
  }
  .brand-mark{width:22px;height:22px;background:var(--white)}
  .brand-name{color:var(--white);font-weight:600;font-size:30px;letter-spacing:2px}
  .headline{
    position:absolute;left:230px;top:30px;width:560px;text-align:center;
  }
  .headline-kicker{color:var(--white);font-weight:800;font-size:36px;line-height:1;white-space:nowrap}
  .headline-main{
    color:var(--lime);font-weight:900;font-size:106px;line-height:1;margin-top:4px;letter-spacing:-1px;
    text-shadow:4px 4px 0 var(--green-dark);
  }
  .headline-sub{color:var(--white);font-weight:500;font-size:23px;margin-top:6px;white-space:nowrap}
  .features{
    position:absolute;left:0;top:267px;width:1000px;height:142px;display:flex;
  }
  .feature{
    flex:1;position:relative;
    background:linear-gradient(90deg,var(--white) 55%,var(--card-shade));
    display:flex;align-items:flex-end;justify-content:center;padding-bottom:22px;
  }
  .feature-label{
    color:var(--ink);font-weight:800;font-size:32px;line-height:1.15;text-align:center;
  }
  .feature-icon{
    position:absolute;left:50%;top:-42px;transform:translateX(-50%);
    width:80px;height:80px;border-radius:50%;
    background:var(--green-dark);border:6px solid var(--lime);
    display:flex;align-items:center;justify-content:center;
  }
  .feature-icon svg{width:46px;height:46px}
  .contact-bar{
    position:absolute;left:0;top:409px;width:1000px;height:88px;background:var(--lime);
  }
  .direction{position:absolute;left:22px;top:7px;width:410px;height:70px}
  .direction-text{
    position:absolute;left:80px;top:28px;height:35px;display:flex;align-items:center;gap:6px;
    color:var(--white);font-family:"Oswald",sans-serif;font-size:25px;white-space:nowrap;
  }
  .contacts{
    position:absolute;left:442px;top:32px;display:flex;align-items:center;gap:10px;
    color:var(--ink);font-weight:600;font-size:16px;white-space:nowrap;
  }
  .divider{width:2px;height:22px;background:var(--ink)}
  .social-dot{width:20px;height:20px;border-radius:50%;border:2px solid var(--ink)}
</style>
</head>
<body>
  <main class="billboard">
    <section class="hero">
      <div class="brand">
        <span class="brand-mark"></span>
        <span class="brand-name">BRINDLE</span>
      </div>
      <div class="headline">
        <p class="headline-kicker">Our New Container Storage</p>
        <h1 class="headline-main">OPENING</h1>
        <p class="headline-sub">Located in the heart of Scunthorpe.</p>
      </div>
    </section>

    <section class="features">
      <div class="feature">
        <div class="feature-icon">
          <svg viewBox="0 0 46 46" fill="none" stroke="#fff" stroke-width="2.5">
            <circle cx="23" cy="23" r="18"/><path d="M23 11v12l8 5"/>
          </svg>
        </div>
        <p class="feature-label">Open<br>24/7</p>
      </div>
      <div class="feature">
        <div class="feature-icon">
          <svg viewBox="0 0 46 46" fill="none" stroke="#fff" stroke-width="2.5">
            <rect x="5" y="13" width="36" height="20"/><path d="M11 16v14M16 16v14M21 16v14M26 16v14M31 16v14M36 16v14"/>
          </svg>
        </div>
        <p class="feature-label">Brand New<br>Containers</p>
      </div>
      <div class="feature">
        <div class="feature-icon">
          <svg viewBox="0 0 46 46" fill="none" stroke="#fff" stroke-width="2.5">
            <path d="M23 4l15 6v11c0 10-7 17-15 21C15 38 8 31 8 21V10z"/>
            <rect x="16" y="21" width="14" height="11"/><path d="M19 21v-4a4 4 0 0 1 8 0v4"/>
          </svg>
        </div>
        <p class="feature-label">On Site<br>Security</p>
      </div>
      <div class="feature">
        <div class="feature-icon">
          <svg viewBox="0 0 46 46" fill="none" stroke="#fff" stroke-width="2.5">
            <circle cx="23" cy="17" r="12"/><path d="M15 26l-6 14 7-3 4 6 3-14M31 26l6 14-7-3-4 6-3-14"/>
            <path d="M26 13c-1-2-6-2-6 1s6 2 6 5-5 3-6 1M23 9v16"/>
          </svg>
        </div>
        <p class="feature-label">Best Prices<br>Guaranteed</p>
      </div>
    </section>

    <section class="contact-bar">
      <svg class="direction" viewBox="0 0 410 70" aria-hidden="true">
        <path d="M0 35L37 0v14h373v44H37v12z" fill="#1d3a1a"/>
      </svg>
      <p class="direction-text">
        <svg width="14" height="18" viewBox="0 0 14 18"><path d="M7 0a7 7 0 0 1 7 7c0 5-7 11-7 11S0 12 0 7a7 7 0 0 1 7-7z" fill="#dcff3c"/><circle cx="7" cy="7" r="2.6" fill="#1d3a1a"/></svg>
        Hollin Row Scunthorpe DN17 3QR
      </p>
      <div class="contacts">
        <svg width="22" height="16" viewBox="0 0 22 16" fill="none" stroke="#1e3320" stroke-width="2"><rect x="1" y="1" width="20" height="14"/><path d="M1 1l10 8 10-8M1 15l7-7M21 15l-7-7"/></svg>
        <span>info@brindlevaults.co.uk</span>
        <span class="divider"></span>
        <span class="social-dot"></span>
        <span>@Brindleselfstorage</span>
      </div>
    </section>
  </main>
</body>
</html>
```